Geschäftspapiere für Rechtsanwaltskanzlei
Zielgruppe
Rechtsanwaltskanzlei als Einzelkanzlei, Schwerpunkt: Immobilienrecht
Aufgabenstellung
Das Design soll modern abstrakt sein und Stärke und Kompromisslosigkeit assoziieren ( wie das bereits vorhandene Logo). Die Informationen im vorhandenen Briefbogen müssen alle übernommen werden.
Wir benötigen 4 Betreffzeilen: Unser Zeichen, Ihr Zeichen, wer ./.wen und kurze Beschreibung des Falles.
Das schwarze Logo soll übernommen werden, gerne hätten wir noch eine zweite Farbe ( rot oder blau ) im Briefbogen in Form von Balken oder Hervorhebung von Text.

```html
<!DOCTYPE html>
<html lang="de">
<head>
<meta charset="utf-8">
<title>Briefbogen Lorenhof Rechtsanwaltskanzlei</title>
<link href="https://fonts.googleapis.com/css2?family=Montserrat:wght@400;500;600&family=Open+Sans:wght@400&display=swap" rel="stylesheet">
<style>
  :root{
    --bg:#dfe3df;
    --paper:#f0f0f2;
    --ink:#1d1d1d;
    --red:#a3150f;
    --band:#e6d6d3;
  }
  html,body{margin:0;padding:0;width:1200px;height:1012px;overflow:hidden;background:var(--bg);}
  body{font-family:"Montserrat",sans-serif;color:var(--ink);}
  .letterhead{position:absolute;left:262px;top:26px;width:676px;height:960px;background:var(--paper);
    box-shadow:0 6px 18px rgba(0,0,0,.18);overflow:hidden;}
  .abs{position:absolute;}
  .rule{position:absolute;height:3px;background:var(--red);}
  .contact{left:75px;top:22px;font-size:11px;line-height:17.5px;}
  .contact-row{display:flex;align-items:center;gap:5px;}
  .contact-row svg{width:10px;height:10px;flex:none;}
  .brand{left:456px;top:46px;width:215px;white-space:nowrap;}
  .brand-mark{display:flex;align-items:flex-end;gap:8px;}
  .brand-square{width:26px;height:26px;background:var(--ink);flex:none;margin-bottom:4px;}
  .brand-name{font-family:"Open Sans",sans-serif;font-size:32px;letter-spacing:0.5px;line-height:1;}
  .brand-sub{font-family:"Open Sans",sans-serif;font-size:14.5px;margin-top:10px;letter-spacing:.1px;}
  .return-line{left:82px;top:144px;font-size:6.6px;line-height:10px;color:#333;}
  .return-line b{font-weight:600;}
  .return-line .sep{color:var(--red);}
  .ref-band{position:absolute;left:428px;width:248px;height:40px;background:var(--band);}
  .ref-label{position:absolute;left:437px;font-size:10.5px;font-weight:500;}
  .lawyer{position:absolute;left:438px;font-size:10.8px;line-height:16px;}
  .lawyer-name{color:var(--red);font-size:12.2px;font-weight:500;margin-bottom:1px;}
  .fold{position:absolute;left:0;width:8px;height:1.5px;background:var(--red);}
  .footer-col{position:absolute;top:881px;font-size:7.6px;line-height:14px;white-space:nowrap;}
  .footer-col b{font-weight:600;}
</style>
</head>
<body>
<main class="letterhead">
  <div class="abs contact">
    <div class="contact-row">
      <svg viewBox="0 0 10 10"><circle cx="5" cy="5" r="5" fill="var(--red)"/><rect x="2.5" y="3.5" width="5" height="3" rx="1" fill="#f0f0f2"/></svg>
      <span>+49 (0) 000 410 20 30</span>
    </div>
    <div class="contact-row">
      <svg viewBox="0 0 10 10"><circle cx="5" cy="5" r="5" fill="var(--red)"/><rect x="2.4" y="3.2" width="5.2" height="3.6" fill="#f0f0f2"/></svg>
      <span>post@lorenhof-kanzlei.de</span>
    </div>
    <div class="contact-row">
      <svg viewBox="0 0 10 10"><circle cx="5" cy="5" r="5" fill="var(--red)"/><circle cx="5" cy="5" r="2.6" fill="none" stroke="#f0f0f2" stroke-width="1"/></svg>
      <span>www.lorenhof-kanzlei.de</span>
    </div>
  </div>
  <div class="rule" style="left:0;top:77px;width:193px;"></div>

  <div class="rule" style="left:456px;top:8px;width:220px;"></div>
  <div class="abs brand">
    <div class="brand-mark">
      <div class="brand-square"></div>
      <div class="brand-name">LORENHOF</div>
    </div>
    <div class="brand-sub">RECHTSANWALTSKANZLEI</div>
  </div>

  <div class="abs return-line">
    <b>Lorenhof Rechtsanwaltskanzlei</b> <span class="sep">|</span> Helena Vorstrand-Kais<br>
    Lindenhofweg 12a <span class="sep">|</span> 50999 Rheinau
  </div>

  <div class="ref-band" style="top:142px;"></div>
  <div class="ref-label" style="top:149px;">Unser Zeichen:</div>
  <div class="ref-label" style="top:186px;">Ihr Zeichen:</div>
  <div class="ref-band" style="top:217px;"></div>
  <div class="ref-label" style="top:223px;">Mandant:</div>
  <div class="ref-label" style="top:262px;">Fallbeschreibung:</div>

  <div class="lawyer" style="top:302px;">
    <div class="lawyer-name">Helena Vorstrand-Kais</div>
    Rechtsanwältin<br>Fachanwältin für Mietrecht und<br>Wohnungseigentumsrecht
  </div>
  <div class="lawyer" style="top:394px;">
    <div class="lawyer-name">Marie Feldhusen</div>
    Rechtsanwältin<br>Fachanwältin für Mietrecht und<br>Wohnungseigentumsrecht
  </div>
  <div class="lawyer" style="top:486px;">
    <div class="lawyer-name">Marie Feldhusen</div>
    Rechtsanwältin<br>Fachanwältin für Mietrecht und<br>Wohnungseigentumsrecht
  </div>
  <div class="lawyer" style="top:578px;">
    <div class="lawyer-name">Marie Feldhusen</div>
    Rechtsanwältin<br>Fachanwältin für Mietrecht und<br>Wohnungseigentumsrecht
  </div>

  <div class="fold" style="top:327px;"></div>
  <div class="fold" style="top:671px;"></div>

  <div class="footer-col" style="left:27px;">
    <b>Büro Nordstadt</b><br>Lindenhofweg 12a<br>50999 Rheinau<br>
    <b>Tel.:</b> +49 (0) 000 4102045<br><b>Fax:</b> +49 (0) 000 410 20 30
  </div>
  <div class="footer-col" style="left:170px;">
    <b>Büro Südufer</b><br>Ahornallee 57<br>50997 Rheinau<br>
    <b>Tel.:</b> +49 (0) 000 518 220 64<br><b>Fax:</b> +49 (0) 000 410 20 30
  </div>
  <div class="footer-col" style="left:305px;">
    <b>Bankverbindung:</b><br>Stadtbank Rheinau<br>
    <b>IBAN</b> DE00123400005678901234<br><b>BIC</b>&nbsp;&nbsp; RHNADE00XXX
  </div>
  <div class="rule" style="left:275px;top:939px;width:401px;"></div>
</main>
</body>
</html>
```